Design a poster that illustrates the six central pillars of our school district's efforts with students. The attached PDF outlines the six main competencies we aim for students to possess upon graduation. Each of the 6 has 3 bullet points for the poster as well. The title is "Profile of a Drifter". Our mascot is this attached winged wheel. The overall concept is that staff take kids when they are young and develop these 6 things when they graduate. Our colors are navy, red, and white. We will make this poster in a variety of sizes in offices, classrooms, and in digital spaces as well. On the PDF - ignore the column that says "Synthesis". That has nothing to do with this poster.

The district is Corvath Falls Public Schools https://www.corvath.k12.example.us/

```html
<!DOCTYPE html>
<html lang="en">
<head>
<meta charset="utf-8">
<title>Profile of a Drifter – Grades 5-12</title>
<link rel="stylesheet" href="https://fonts.googleapis.com/css2?family=Baloo+2:wght@600;700&family=Saira:wght@300;800&display=swap">
<style>
  :root {
    --navy: #10113a;
    --red: #a41e26;
    --white: #ffffff;
    --ink: #1f1f3a;
    --blue: #14aee8;
    --crimson: #e5333a;
    --green: #0aa94f;
    --orange: #f18a2f;
    --lavender: #9e98cc;
  }
  * { margin: 0; padding: 0; box-sizing: border-box; }
  html, body { width: 884px; height: 1200px; overflow: hidden; background: var(--navy); }
  .poster { position: relative; width: 884px; height: 1200px; background: var(--navy); }
  .frame {
    position: absolute; left: 67px; top: 60px; width: 750px; height: 1080px;
    background: var(--white); border: 10px solid var(--red); border-radius: 38px;
  }
  .district-mark {
    position: absolute; left: 0; top: 118px; width: 884px;
    display: flex; align-items: center; justify-content: center; gap: 12px;
    font-family: "Baloo 2", sans-serif; font-weight: 700; font-size: 26px; color: var(--red);
  }
  .district-mark .dot { width: 30px; height: 30px; border-radius: 50%; background: var(--red); }
  .title-band {
    position: absolute; left: 78px; top: 246px; width: 739px; height: 71px;
    background: var(--red); display: flex; align-items: center; justify-content: center;
    font-family: "Saira", sans-serif; color: var(--white); font-size: 52px; line-height: 1;
  }
  .title-band .light { font-weight: 300; margin-right: 12px; }
  .title-band .bold { font-weight: 800; }
  .grades-tab {
    position: absolute; left: 476px; top: 324px; width: 341px; height: 38px;
    background: var(--navy); border-radius: 22px 0 0 22px;
    font-family: "Saira", sans-serif; font-weight: 800; color: var(--white);
    font-size: 28px; letter-spacing: 3px; line-height: 38px; text-align: center;
  }
  .mini-mark {
    position: absolute; display: flex; align-items: center; gap: 5px;
    font-family: "Baloo 2", sans-serif; font-weight: 700; font-size: 12px; color: var(--navy);
  }
  .mini-mark .dot { width: 18px; height: 18px; border-radius: 50%; background: var(--navy); }
  .mini-mark.top-left { left: 140px; top: 372px; }
  .mini-mark.bottom-right { left: 644px; top: 1048px; }
  .pathway { position: absolute; left: 0; top: 0; }
  .pillar-name {
    position: absolute; font-family: "Baloo 2", sans-serif; font-weight: 700;
    font-size: 22px; line-height: 26px; letter-spacing: -0.3px;
    padding: 0 5px; background: var(--white);
    transform: translateY(-50%); white-space: nowrap;
  }
  .pillar-name.communicator { left: 534px; top: 408px; color: var(--blue); }
  .pillar-name.critical { left: 174px; top: 514px; color: var(--crimson); }
  .pillar-name.responsible { left: 534px; top: 618px; color: var(--green); }
  .pillar-name.adaptable { left: 174px; top: 723px; color: var(--orange); }
  .pillar-name.collaborator { left: 534px; top: 840px; color: var(--crimson); }
  .pillar-name.compassionate { left: 174px; top: 944px; color: var(--lavender); }
  .traits {
    position: absolute; left: 155px; list-style: none;
    font-family: "Baloo 2", sans-serif; font-weight: 600; color: var(--ink);
    letter-spacing: -0.3px; white-space: nowrap;
  }
  .traits li { position: relative; padding-left: 14px; }
  .traits li::before {
    content: ""; position: absolute; left: 0; top: 50%; margin-top: -4px;
    width: 6px; height: 6px; border-radius: 50%; background: var(--ink);
  }
  .traits li.wrap::before { top: 10px; margin-top: 0; }
  .traits.communicator { top: 425px; font-size: 19.5px; line-height: 21.5px; }
  .traits.critical { top: 531px; font-size: 18.5px; line-height: 19.7px; }
  .traits.responsible { top: 642px; font-size: 19.3px; line-height: 22px; }
  .traits.adaptable { top: 744px; font-size: 17.5px; line-height: 21px; letter-spacing: -0.4px; }
  .traits.collaborator { top: 862px; font-size: 18px; line-height: 21.3px; }
  .traits.compassionate { top: 963px; font-size: 17.5px; line-height: 24px; letter-spacing: -0.4px; }
</style>
</head>
<body>
<main class="poster">
  <div class="frame"></div>

  <div class="district-mark"><span class="dot"></span>Corvath Falls Public Schools</div>

  <h1 class="title-band"><span class="light">Profile of a</span><span class="bold">DRIFTER</span></h1>
  <div class="grades-tab">GRADES 5-12</div>

  <div class="mini-mark top-left"><span class="dot"></span>Corvath Falls</div>
  <div class="mini-mark bottom-right"><span class="dot"></span>Corvath Falls</div>

  <svg class="pathway" width="884" height="1200" viewBox="0 0 1652 2243" fill="none" stroke-width="7" stroke-linecap="round" aria-hidden="true">
    <path stroke="var(--blue)" d="M390 763 H995 M1280 763 H1312 A98.5 98.5 0 0 1 1312 960 H620"/>
    <path stroke="var(--crimson)" d="M322 960 H318 A98.5 98.5 0 0 0 318 1157 H990"/>
    <path stroke="var(--green)" d="M1238 1155 H1312 A98.5 98.5 0 0 1 1312 1352 H525"/>
    <path stroke="var(--orange)" d="M322 1352 H318 A109 109 0 0 0 318 1570 H990"/>
    <path stroke="var(--crimson)" d="M1250 1568 H1312 A98.5 98.5 0 0 1 1312 1765 H620"/>
    <path stroke="var(--lavender)" d="M322 1765 H318 A98.5 98.5 0 0 0 318 1962 H1170"/>
  </svg>

  <h2 class="pillar-name communicator">Communicator</h2>
  <ul class="traits communicator">
    <li>Expresses ideas clearly and respectfully (written &amp; verbal).</li>
    <li>Listens actively and understands diverse perspectives.</li>
    <li>Adjusts communication to suit the audience and context.</li>
  </ul>

  <h2 class="pillar-name critical">Critical Thinker</h2>
  <ul class="traits critical">
    <li>Questions, analyzes, and evaluates information from multiple sources.</li>
    <li>Identifies and solves complex problems creatively.</li>
    <li class="wrap">Uses evidence and diverse perspectives to form reasoned conclusions<br>and make informed decisions</li>
  </ul>

  <h2 class="pillar-name responsible">Responsible</h2>
  <ul class="traits responsible">
    <li>Takes ownership of actions, choices, and commitments.</li>
    <li>Manages time, resources, and self to meet expectations.</li>
    <li>Acts with integrity and advocates for self and others.</li>
  </ul>

  <h2 class="pillar-name adaptable">Adaptable</h2>
  <ul class="traits adaptable">
    <li>Responds productively to new situations, challenges, and feedback.</li>
    <li>Learns from new experiences and applies prior knowledge in evolving contexts.</li>
    <li class="wrap">Adjusts behavior and approach to effectively engage with<br>diverse groups and environments.</li>
  </ul>

  <h2 class="pillar-name collaborator">Collaborator</h2>
  <ul class="traits collaborator">
    <li>Contributes effectively and cooperatively to shared goals</li>
    <li>Listens actively and values diverse ideas and perspectives.</li>
    <li>Engages respectfully, compromising and leading when appropriate</li>
  </ul>

  <h2 class="pillar-name compassionate">Compassionate</h2>
  <ul class="traits compassionate">
    <li>Understands and acknowledges others' feelings, perspectives, and experiences.</li>
    <li>Responds with kindness, patience, and support.</li>
    <li>Seeks to connect with and contribute positively to the well-being of others</li>
  </ul>
</main>
</body>
</html>
```